Renata Quisby

Luxury And Style -

Black - White & Gold

Target Market(s)

Fashion

Industry/Entity Type

Fashion

Requirements
Must have
• High-End
Nice to have
• We will Print on Silk Paper

```html
<!DOCTYPE html>
<html lang="en">
<head>
<meta charset="UTF-8">
<title>Renata Quisby — Letterhead</title>
<link rel="stylesheet" href="https://fonts.googleapis.com/css2?family=Poppins:wght@400;500&display=swap">
<style>
  :root {
    --paper: #ffffff;
    --ink: #111111;
    --rule: #1c1c1c;
    --brand-black: #0b0b0b;
    --gold: #c9a145;
  }
  html, body {
    margin: 0;
    padding: 0;
    width: 848px;
    height: 1200px;
    overflow: hidden;
    background: var(--paper);
  }
  .letterhead {
    position: relative;
    width: 848px;
    height: 1200px;
    background: var(--paper);
    font-family: "Poppins", sans-serif;
    color: var(--ink);
  }
  .brand-block {
    position: absolute;
    left: 33px;
    top: 0;
    width: 237px;
    height: 193px;
    background: var(--brand-black);
    display: flex;
    align-items: center;
    justify-content: center;
  }
  .brand-name {
    margin: 0;
    font-family: "Poppins", sans-serif;
    font-weight: 500;
    font-size: 19px;
    letter-spacing: 2px;
    text-transform: uppercase;
    color: var(--gold);
  }
  .header-rule {
    position: absolute;
    left: 270px;
    top: 104px;
    width: 543px;
    height: 2px;
    background: var(--rule);
  }
  .footer-rule {
    position: absolute;
    left: 35px;
    top: 1082px;
    width: 778px;
    height: 2px;
    background: var(--rule);
  }
  .social-row {
    position: absolute;
    left: 0;
    top: 0;
  }
  .contact {
    position: absolute;
    top: 1110px;
    margin: 0;
    font-size: 14px;
    font-weight: 500;
    letter-spacing: 1.6px;
    line-height: 27px;
    text-transform: uppercase;
  }
  .contact--address { left: 362px; }
  .contact--web { left: 556px; }
  .contact-divider {
    position: absolute;
    left: 531px;
    top: 1112px;
    width: 2px;
    height: 46px;
    background: var(--rule);
  }
</style>
</head>
<body>
  <div class="letterhead">
    <header>
      <div class="brand-block">
        <p class="brand-name">Renata Quisby</p>
      </div>
      <div class="header-rule"></div>
    </header>

    <footer>
      <div class="footer-rule"></div>
      <svg class="social-row" width="848" height="1200" viewBox="0 0 848 1200" aria-label="Social profiles">
        <g fill="none" stroke="#111111" stroke-width="2.6">
          <circle cx="92" cy="1136" r="19"/>
          <circle cx="196" cy="1136" r="19"/>
          <circle cx="297" cy="1136" r="19"/>
        </g>
        <g stroke="#111111" stroke-width="2">
          <line x1="144" y1="1116" x2="144" y2="1156"/>
          <line x1="250" y1="1116" x2="250" y2="1156"/>
        </g>
      </svg>
      <p class="contact contact--address">Lorem Ipsum, 123<br>+12 345 678 910</p>
      <div class="contact-divider"></div>
      <p class="contact contact--web">www.yourwebsite.com<br>yourmail@email.com</p>
    </footer>
  </div>
</body>
</html>
```